Environmental Group Website Template

We want a website template for an environmental cause. The website should have a dark content area that is transparent. The website text and icons are white.
The background is a nature scene. The background image repeats.
Industry/Entity Type
Group

```html
<!DOCTYPE html>
<html lang="en">
<head>
<meta charset="utf-8">
<title>Tidewater Group — Environmental Group Website</title>
<link rel="stylesheet" href="https://fonts.googleapis.com/css2?family=Source+Sans+3:wght@400;600;700&display=swap">
<style>
  :root {
    --sky-top: #9fb6c8;
    --sky-low: #d9dcd4;
    --marsh: #6f8a3a;
    --marsh-dark: #4a5e2a;
    --water: #4d6580;
    --water-deep: #2f4660;
    --header-bg: #47484a;
    --nav-bg: #3a4729;
    --accent: #7ea20c;
    --arrow-bg: #4f7a1c;
    --content-bg: rgba(42, 30, 14, 0.86);
    --footer-bg: #2a2a2a;
    --text: #ffffff;
    --muted: #8a8a8a;
  }
  * { box-sizing: border-box; margin: 0; padding: 0; }
  html, body { width: 1200px; height: 1148px; overflow: hidden; }
  body {
    font-family: "Source Sans 3", "Myriad Pro", sans-serif;
    color: var(--text);
    position: relative;
  }
  .backdrop {
    position: absolute; inset: 0;
    background:
      linear-gradient(180deg,
        var(--sky-top) 0%, var(--sky-low) 31%,
        var(--marsh) 34%, var(--marsh-dark) 40%,
        var(--water) 48%, var(--marsh) 62%,
        var(--water-deep) 70%, var(--water) 86%, var(--marsh) 100%);
  }
  .page {
    position: absolute; left: 183px; top: 0; width: 836px; height: 1148px;
  }
  .site-header {
    position: absolute; left: 0; top: 0; width: 100%; height: 71px;
    background: var(--header-bg);
  }
  .brand {
    position: absolute; left: 24px; top: 22px;
    display: flex; align-items: center; gap: 9px;
    font-size: 15px; font-weight: 600; color: var(--text);
  }
  .brand-mark { width: 22px; height: 22px; border-radius: 50%; background: var(--text); }
  .search {
    position: absolute; left: 615px; top: 20px; width: 203px; height: 29px;
    display: flex;
  }
  .search-field {
    flex: 1; background: #fff; color: var(--muted);
    font-size: 12px; font-style: italic; padding: 7px 9px; line-height: 15px;
  }
  .search-button {
    width: 35px; background: var(--accent);
    display: flex; align-items: center; justify-content: center;
  }
  .main-nav {
    position: absolute; left: 0; top: 71px; width: 100%; height: 50px;
    background: var(--nav-bg);
  }
  .main-nav a {
    position: absolute; top: 11px; transform: translateX(-50%);
    color: var(--text); text-decoration: none; font-size: 21px; line-height: 25px;
  }
  .hero {
    position: absolute; left: 0; top: 121px; width: 100%; height: 397px;
    background: linear-gradient(100deg, #e4eea8 0%, #c9d98a 14%, #f1c9a6 34%, #e6a783 58%, #b8704a 82%, #6e3b22 100%);
  }
  .hero-arrow {
    position: absolute; top: 163px; width: 36px; height: 36px;
    background: var(--arrow-bg);
    display: flex; align-items: center; justify-content: center;
  }
  .hero-arrow.prev { left: -1px; }
  .hero-arrow.next { right: 0; }
  .hero-dots {
    position: absolute; left: 375px; top: 372px; display: flex; gap: 9px;
  }
  .hero-dots span {
    width: 13px; height: 13px; border-radius: 50%; border: 1.5px solid rgba(255,255,255,0.8);
  }
  .hero-dots span.active { border-color: #333; background: rgba(255,255,255,0.6); }
  .content {
    position: absolute; left: 0; top: 518px; width: 100%; height: 488px;
    background: var(--content-bg);
  }
  .intro {
    position: absolute; left: 84px; top: 30px; width: 668px;
    text-align: center; font-size: 20px; line-height: 23.5px;
  }
  .feature {
    position: absolute; top: 152px; width: 230px; text-align: center;
    transform: translateX(-50%);
  }
  .feature-art {
    width: 140px; height: 116px; margin: 0 auto;
    background: rgba(255,255,255,0.9); border-radius: 18px;
  }
  .feature-title { margin-top: 31px; font-size: 21px; font-weight: 600; line-height: 24px; }
  .feature-text {
    margin: 10px auto 0; width: 218px;
    font-size: 11.5px; font-weight: 700; line-height: 14.2px;
  }
  .site-footer {
    position: absolute; left: 0; top: 1006px; width: 100%; height: 142px;
    background: var(--footer-bg);
  }
  .footer-nav a {
    position: absolute; top: 18px; transform: translateX(-50%);
    color: var(--text); text-decoration: none;
    font-size: 9.5px; font-weight: 700; text-transform: uppercase;
  }
  .social {
    position: absolute; left: 24px; top: 45px; display: flex; gap: 11px;
  }
  .social a { width: 35px; height: 35px; display: block; }
  .footer-note {
    position: absolute; left: 381px; top: 46px; width: 420px;
    font-size: 10px; font-weight: 700; line-height: 11.5px;
  }
  .copyright {
    position: absolute; left: 0; top: 114px; width: 100%; text-align: center;
    font-size: 10px; font-weight: 700;
  }
</style>
</head>
<body>
  <div class="backdrop" role="img" aria-label="Repeating nature scene: sky over green salt marsh and open water"></div>

  <div class="page">
    <header class="site-header">
      <div class="brand"><span class="brand-mark"></span>Tidewater Group</div>
      <div class="search">
        <div class="search-field">Search this Site...</div>
        <div class="search-button">
          <svg width="20" height="20" viewBox="0 0 20 20" aria-hidden="true">
            <circle cx="8" cy="8" r="6" fill="none" stroke="#fff" stroke-width="2.6"/>
            <line x1="12.5" y1="12.5" x2="18" y2="18" stroke="#fff" stroke-width="3" stroke-linecap="round"/>
          </svg>
        </div>
      </div>
    </header>

    <nav class="main-nav">
      <a href="#" style="left:60px">Home</a>
      <a href="#" style="left:163px">About</a>
      <a href="#" style="left:278px">Explore</a>
      <a href="#" style="left:410px">Challenges</a>
      <a href="#" style="left:552px">Solutions</a>
      <a href="#" style="left:673px">Events</a>
      <a href="#" style="left:775px">News</a>
    </nav>

    <section class="hero" role="img" aria-label="Photo slide: a young woman drinking a glass of clean water">
      <div class="hero-arrow prev">
        <svg width="14" height="22" viewBox="0 0 14 22" aria-hidden="true"><polyline points="11,2 3,11 11,20" fill="none" stroke="#fff" stroke-width="2"/></svg>
      </div>
      <div class="hero-arrow next">
        <svg width="14" height="22" viewBox="0 0 14 22" aria-hidden="true"><polyline points="3,2 11,11 3,20" fill="none" stroke="#fff" stroke-width="2"/></svg>
      </div>
      <div class="hero-dots"><span class="active"></span><span></span><span></span><span></span></div>
    </section>

    <main class="content">
      <p class="intro">Lorem ipsum dolor sit amet, eros eu purus tortor turpis, porttitor urna quis felis purus ab, eleifend imperdiet aut congue lectus, dolor tempor vitae, augue curabi­tur fusce erat vel rutrum. Nascetur donec velit nisl vitae. Quam luctus tellus donec dolores ac. Aliquam lorem eget, molestie elit volupt.</p>

      <article class="feature" style="left:145px">
        <div class="feature-art" role="img" aria-label="Icon: volunteer with raised arms and a leaf"></div>
        <h2 class="feature-title">Volunteer</h2>
        <p class="feature-text">Lorem ipsum dolor sit amet, tempor quis nisl est pellentesque felis ut, placerat nulla amet sed mauris suspendisse, nibh velit velit venenatis sed libero cras, ipsum hen­drerit auctor diam non dolor pulvinar, quis­que nunc autus accumsan, rhoncus velit lorem pede morbi mauris augue.</p>
      </article>

      <article class="feature" style="left:418px">
        <div class="feature-art" role="img" aria-label="Icon: hand pressing a donate sign"></div>
        <h2 class="feature-title">Support Our Work</h2>
        <p class="feature-text">Lorem ipsum dolor sit amet, tempor quis nisl est pellentesque felis ut, placerat nulla amet sed mauris suspendisse, nibh velit velit venenatis sed libero cras, ipsum hen­drerit auctor diam non dolor pulvinar, quis­que nunc autus accumsan, rhoncus velit lorem pede morbi mauris augue.</p>
      </article>

      <article class="feature" style="left:689px">
        <div class="feature-art" role="img" aria-label="Icon: group of people holding protest signs"></div>
        <h2 class="feature-title">Make Your Voice Heard</h2>
        <p class="feature-text">Lorem ipsum dolor sit amet, tempor quis nisl est pellentesque felis ut, placerat nulla amet sed mauris suspendisse, nibh velit velit venenatis sed libero cras, ipsum hen­drerit auctor diam non dolor pulvinar, quis­que nunc autus accumsan, rhoncus velit lorem pede morbi mauris augue.</p>
      </article>
    </main>

    <footer class="site-footer">
      <nav class="footer-nav">
        <a href="#" style="left:212px">Home</a>
        <a href="#" style="left:268px">About</a>
        <a href="#" style="left:332px">Explorer</a>
        <a href="#" style="left:414px">Challenges</a>
        <a href="#" style="left:493px">Solutions</a>
        <a href="#" style="left:564px">Events</a>
        <a href="#" style="left:625px">News</a>
      </nav>
      <div class="social">
        <a href="#" aria-label="Social link 1" style="background:#d34836"></a>
        <a href="#" aria-label="Social link 2" style="background:#3b5998"></a>
        <a href="#" aria-label="Social link 3" style="background:#4aa3df"></a>
        <a href="#" aria-label="Social link 4" style="background:#1b86bc"></a>
        <a href="#" aria-label="Social link 5" style="background:#c4302b"></a>
        <a href="#" aria-label="Social link 6" style="background:#c8232c"></a>
        <a href="#" aria-label="Social link 7" style="background:#f26522"></a>
      </div>
      <p class="footer-note">Lorem ipsum dolor sit amet, diam ac, orci libero pede integer lobortis, donec hac, mi arcu tincidunt nisl pulvinar magna. Neque vitae aliquam nec, lorem sed proin cras nullam mi commodo, dapibus imperdiet fermentum mattis orci, volutpat massa wisi vel consequat.</p>
      <p class="copyright">© 2015. All righs Reserved | Environmental Group Website</p>
    </footer>
  </div>
</body>
</html>
```